Flyer-Design für plastische Chirurgin
Zielgruppe
Ich bin Plastische Chirurgin und mache vornehmlich Ästhetik (Unterspritzungen und Operationen).
Die Zielgruppe schließt erstmal jeden ein.
Aufgabenstellung
Es handelt sich um die Erstellung von 4 Flyern, die ästhetische Behandlungen beschreiben. Die Flyer sollen hochwertig wirken und in einheitlichem Design -angelehnt an das Firmenlogo- erstellt werden. Das Design soll clean sein, nicht effekthaschend sondern ästhetisch ansprechend. Der Auftrag schließt die Erstellung von 5 auf allen Flyern benutzen icons mit ein (Betäubung, OP Dauer, Schmerzen, Schonung, Haltbarkeit).
Es darf gerne nach passenden Bildern gesucht werden. Hier bevorzuge ich Illustrationen vor echten Bildern, bin aber nicht festgelegt.
Der Auftrag kann zu einer dauerhaften Zusammenarbeit führen (corporate design, pixo und vidorama design, Visitenkarten, DinA4 Mappen usw). Das Logo ist bereits erstellt.

```html
<!DOCTYPE html>
<html lang="de">
<head>
<meta charset="utf-8">
<title>Lumenhaut – Flyer Körperchirurgie</title>
<link href="https://fonts.googleapis.com/css2?family=Playfair+Display:wght@400;600;700&family=Source+Sans+3:wght@300;400;600;700&display=swap" rel="stylesheet">
<style>
  :root{
    --bg:#e9e9e9;
    --paper:#ffffff;
    --accent:#e0451f;
    --ink:#262626;
    --body:#4a4a4a;
    --soft:#8a8a8a;
    --photo-a:#cfcbe0;
    --photo-b:#c49a80;
  }
  *{box-sizing:border-box;margin:0;padding:0}
  html,body{width:1200px;height:900px;overflow:hidden;background:var(--bg)}
  body{position:relative;font-family:"Source Sans 3",sans-serif;color:var(--body)}

  .spread{position:absolute;top:240px;width:576px;height:420px;background:var(--paper);display:flex;box-shadow:0 1px 0 rgba(0,0,0,.04)}
  .spread--outside{left:14px}
  .spread--inside{left:610px}
  .panel{position:relative;width:192px;height:100%;padding:36px 14px 0 24px}
  .panel + .panel{border-left:1px solid #f0f0f0}

  .band{position:absolute;left:0;right:0;bottom:0;height:28px;background:var(--accent)}

  .section-title{position:relative;font-family:"Playfair Display",serif;font-weight:600;font-size:8.6px;line-height:1.15;color:var(--ink);margin-bottom:6px}
  .section-title::before{content:"";position:absolute;left:-6px;top:2px;width:16px;height:6px;background:var(--accent);transform:rotate(-14deg);opacity:.9;z-index:-1}
  .section-title span{position:relative}
  .sub-title{font-family:"Playfair Display",serif;font-size:6.4px;color:var(--ink);margin:9px 0 4px}
  p,li{font-size:4.6px;line-height:1.45}
  p{margin-bottom:4px}
  b{color:var(--ink);font-weight:700}

  .offer-list{list-style:none;margin:0 0 0 8px}
  .offer-list li{font-size:4.8px;line-height:2.5}
  .offer-block{position:absolute;left:24px}

  .arrow-list{list-style:none;margin:4px 0 5px}
  .arrow-list li{position:relative;padding-left:7px;margin-bottom:3px}
  .arrow-list li::before{content:"";position:absolute;left:0;top:1px;border-left:3.5px solid var(--accent);border-top:2.4px solid transparent;border-bottom:2.4px solid transparent}
  .arrow-list--inline{display:flex;gap:14px}

  .icon-row{display:flex;gap:2px;margin:8px 0 10px}
  .icon{width:27px;text-align:center}
  .icon svg{display:block;margin:0 auto 2px}
  .icon strong{display:block;font-size:3.5px;font-weight:700;color:var(--ink);letter-spacing:.1px}
  .icon small{display:block;font-size:2.9px;color:var(--soft)}

  .address{position:absolute;left:24px;top:198px;font-size:4.8px;line-height:1.45}
  .address .name{font-family:"Playfair Display",serif;font-size:6.6px;color:var(--ink)}
  .address .gap{margin-top:6px}

  .brand{font-family:"Source Sans 3",sans-serif;font-weight:300;color:var(--ink);letter-spacing:.4px}
  .cover .brand{position:absolute;top:38px;right:22px;font-size:15px}
  .cover-title{position:absolute;left:16px;top:104px;font-family:"Playfair Display",serif;font-weight:600;font-size:13.4px;line-height:1.2;color:var(--ink)}
  .cover-list{position:absolute;left:16px;top:156px;list-style:none}
  .cover-list li{position:relative;font-family:"Playfair Display",serif;font-weight:600;font-size:8.4px;line-height:1.3;color:var(--ink);padding-left:6px}
  .cover-list li.arrow::before{content:"";position:absolute;left:0;top:2.6px;border-left:3.6px solid var(--accent);border-top:2.8px solid transparent;border-bottom:2.8px solid transparent}
  .cta{position:absolute;left:128px;top:197px;width:46px;height:46px;border-radius:50%;background:var(--accent);color:#fff;font-family:"Playfair Display",serif;font-size:4.4px;line-height:1.2;text-align:center;display:flex;align-items:center;justify-content:center;z-index:2}
  .cover-photo{position:absolute;left:0;right:0;top:236px;bottom:28px;background:linear-gradient(160deg,var(--photo-a) 0%,#d8d4e4 40%,var(--photo-b) 100%)}

  .inside-brand{position:absolute;right:16px;bottom:22px;font-size:8px}
</style>
</head>
<body>

<!-- Outside of the trifold -->
<section class="spread spread--outside">
  <div class="panel">
    <div class="offer-block" style="top:54px">
      <h2 class="section-title"><span>Operationen für Frau und Mann</span></h2>
      <ul class="offer-list">
        <li>Gesichtschirurgie</li>
        <li>Körperchirurgie</li>
        <li>Weibliche und männliche Brustchirurgie</li>
        <li>Intimchirurgie</li>
        <li>Haartransplantationen</li>
      </ul>
    </div>
    <div class="offer-block" style="top:168px">
      <h2 class="section-title"><span>Behandlungen für Frau und Mann</span></h2>
      <ul class="offer-list">
        <li><b>Gesicht, Hals und Decolletée</b></li>
        <li>Unterspritzungen mit Nervolin und Fillern</li>
        <li>Innovative Hautverbesserung mit Peelings</li>
        <li>Fäden und Radiofrequenzbehandlungen</li>
      </ul>
    </div>
    <div class="offer-block" style="top:264px">
      <h2 class="section-title"><span>Körper</span></h2>
      <ul class="offer-list">
        <li>Fetteinfrierungen durch Kryolipolyse</li>
        <li>Anticellulitebehandlungen mit Cellvira</li>
        <li>Antischweißbehandlungen mit Sudaclear oder</li>
        <li>Nervolin</li>
      </ul>
    </div>
  </div>

  <div class="panel">
    <address class="address" style="font-style:normal">
      <div class="name">Lumenhaut</div>
      <div>Lindenallee 14</div>
      <div>54321 Beispielstadt</div>
      <div class="gap">Telefon 0123 / 987650</div>
      <div>kontakt@lumenhaut.de</div>
    </address>
  </div>

  <div class="panel cover">
    <div class="brand">Lumenhaut</div>
    <h1 class="cover-title">Körperchirurgie<br>für Frau und Mann</h1>
    <ul class="cover-list">
      <li class="arrow">Fettabsaugungen und</li>
      <li>Eigenfett-Tansfer</li>
      <li class="arrow">Lipödem</li>
      <li class="arrow">Brustchirurgie</li>
      <li class="arrow">Straffungen</li>
    </ul>
    <div class="cta">JETZT<br>TERMIN<br>VEREINBAREN</div>
    <div class="cover-photo" role="img" aria-label="Foto: Frauenkörper in heller Unterwäsche mit eingezeichneten Schnittlinien an Taille und Oberschenkel"></div>
  </div>

  <div class="band"></div>
</section>

<!-- Inside of the trifold -->
<section class="spread spread--inside">
  <div class="panel">
    <h2 class="section-title"><span>Fettabsaugung/ Eigenfett-<br>Transfer/ Lipödem</span></h2>
    <h3 class="sub-title">Liposuktion/ Fettabsaugung</h3>
    <p>Die Liposuktion eignet sich zur <b>Figuroptimierung</b> und zur <b>Entfernung größerer Fettmengen</b>. Der Wunsch danach kann viele Ursachen haben:</p>
    <ul class="arrow-list">
      <li>Wenn Sport und gesunde Ernährung nicht zur Wunschfigur führen</li>
      <li>Wenn die Fettverteilung zu unausgeglichenen Proportionen führt</li>
      <li>Bei ungewünschten Veränderungen durch hormonellen Einfluss</li>
    </ul>
    <p>Durch die Fettabsaugung werden Fettzellen endgültig entfernt. Angepasst an Ihre Wünsche kann so eine dauerhafte Optimierung erzielt werden. Die Wahl der Methode ist dabei von großer Bedeutung und wird gemeinsam im Gespräch festgelegt.</p>
    <p>Spezielle Anti-Cellulite Behandlungen können zusätzlich für ein ebenmäßiges Hautbild sorgen.</p>
    <p>Durch die sanfte Wasserstrahlmethode können auch <b>Lipödempatientinnen lymphbahnschonend</b> operiert werden.</p>
    <div class="icon-row">
      <div class="icon"><svg width="10" height="10" viewBox="0 0 10 10"><circle cx="5" cy="5" r="5" fill="#e0451f"/><path d="M2.8 7.2l3.6-3.6M5.6 2.6l1.8 1.8" stroke="#fff" stroke-width=".8" stroke-linecap="round"/></svg><strong>BETÄUBUNG</strong><small>Vollnarkose</small></div>
      <div class="icon"><svg width="10" height="10" viewBox="0 0 10 10"><circle cx="5" cy="5" r="5" fill="#e0451f"/><circle cx="5" cy="5" r="2.8" fill="none" stroke="#fff" stroke-width=".7"/><path d="M5 3.6V5l1 .8" stroke="#fff" stroke-width=".7" fill="none" stroke-linecap="round"/></svg><strong>DAUER</strong><small>1–2 Stunden</small></div>
      <div class="icon"><svg width="10" height="10" viewBox="0 0 10 10"><circle cx="5" cy="5" r="5" fill="#e0451f"/><path d="M5.6 2L3.4 5.3h1.7L4.4 8l2.2-3.3H4.9z" fill="#fff"/></svg><strong>SCHMERZEN</strong><small>gut behandelbar</small></div>
      <div class="icon"><svg width="10" height="10" viewBox="0 0 10 10"><circle cx="5" cy="5" r="5" fill="#e0451f"/><path d="M3.3 3.3l3.4 3.4M6.7 3.3L3.3 6.7" stroke="#fff" stroke-width=".8" stroke-linecap="round"/></svg><strong>SCHONUNG</strong><small>2–3 Wochen</small></div>
      <div class="icon"><svg width="10" height="10" viewBox="0 0 10 10"><circle cx="5" cy="5" r="5" fill="#e0451f"/><path d="M7.2 5A2.2 2.2 0 1 1 6.4 3.3" stroke="#fff" stroke-width=".8" fill="none" stroke-linecap="round"/><path d="M6.8 2.3v1.4H5.4" stroke="#fff" stroke-width=".7" fill="none"/></svg><strong>HALTBARKEIT</strong><small>dauerhaft</small></div>
    </div>
    <h3 class="sub-title">Eigenfett-Transfer/ Liposkulptur</h3>
    <p>Liposkulptur beschreibt die Kombination aus Absaugung und Eigenfetteinspritzung. Das gewonnene Fett kann zum <b>Volumenaufbau</b> verwendet werden für:</p>
    <ul class="arrow-list arrow-list--inline">
      <li>Gesicht</li><li>Brust</li><li>Gesäß</li><li>Narben</li>
    </ul>
    <p>Durch die gewebeschonende <b>Wasserstrahlmethode</b> ist die Anwachsquote des Eigenfettes sehr hoch. Die Ergebnisse sind natürlich und dauerhaft.</p>
  </div>

  <div class="panel">
    <h2 class="section-title"><span>Weibliche Brustchirurgie</span></h2>
    <h3 class="sub-title">Brustvergrößerung</h3>
    <p>Im Rahmen einer persönlichen Beratung werden Ihre Wünsche besprochen. Es gibt drei Möglichkeiten der Brustvergrößerung:</p>
    <ul class="arrow-list">
      <li>Implantate</li>
      <li>Eigenfett</li>
      <li>Hybridvergrößerung mit Implantaten und Eigenfett</li>
    </ul>
    <p>Jede Methode hat unterschiedliche Vorteile. Welche davon am besten geeignet ist, legen wir gemeinsam fest. Es werden nur Markenimplantate verwendet.</p>
    <h3 class="sub-title">Bruststraffung</h3>
    <p>Die Brust kann nicht nur gestrafft, sondern in gleicher Sitzung formverändert werden. Je nach Wunsch ist eine <b>Volumenerhaltung</b> oder <b>straffende Verkleinerung</b> möglich.</p>
    <h3 class="sub-title">Brustverkleinerung</h3>
    <p>Patientinnen, die sich für eine Brustverkleinerung entscheiden, haben oft jahrelang über den Eingriff nachgedacht. Sie ist ein sehr sensibler Eingriff, bei dem Form und Größe im Vordergrund stehen.</p>
    <div class="icon-row">
      <div class="icon"><svg width="10" height="10" viewBox="0 0 10 10"><circle cx="5" cy="5" r="5" fill="#e0451f"/><path d="M2.8 7.2l3.6-3.6M5.6 2.6l1.8 1.8" stroke="#fff" stroke-width=".8" stroke-linecap="round"/></svg><strong>BETÄUBUNG</strong><small>Vollnarkose</small></div>
      <div class="icon"><svg width="10" height="10" viewBox="0 0 10 10"><circle cx="5" cy="5" r="5" fill="#e0451f"/><circle cx="5" cy="5" r="2.8" fill="none" stroke="#fff" stroke-width=".7"/><path d="M5 3.6V5l1 .8" stroke="#fff" stroke-width=".7" fill="none" stroke-linecap="round"/></svg><strong>DAUER</strong><small>1–2 Stunden</small></div>
      <div class="icon"><svg width="10" height="10" viewBox="0 0 10 10"><circle cx="5" cy="5" r="5" fill="#e0451f"/><path d="M5.6 2L3.4 5.3h1.7L4.4 8l2.2-3.3H4.9z" fill="#fff"/></svg><strong>SCHMERZEN</strong><small>gut behandelbar</small></div>
      <div class="icon"><svg width="10" height="10" viewBox="0 0 10 10"><circle cx="5" cy="5" r="5" fill="#e0451f"/><path d="M3.3 3.3l3.4 3.4M6.7 3.3L3.3 6.7" stroke="#fff" stroke-width=".8" stroke-linecap="round"/></svg><strong>SCHONUNG</strong><small>2–3 Wochen</small></div>
      <div class="icon"><svg width="10" height="10" viewBox="0 0 10 10"><circle cx="5" cy="5" r="5" fill="#e0451f"/><path d="M7.2 5A2.2 2.2 0 1 1 6.4 3.3" stroke="#fff" stroke-width=".8" fill="none" stroke-linecap="round"/><path d="M6.8 2.3v1.4H5.4" stroke="#fff" stroke-width=".7" fill="none"/></svg><strong>HALTBARKEIT</strong><small>dauerhaft</small></div>
    </div>
    <h2 class="section-title"><span>Männliche Brustchirurgie/<br>Gynäkomastie</span></h2>
    <p>Die Ausbildung einer vergrößerten männlichen Brust ist nicht ungewöhnlich. Die Ursachen sind unter anderem:</p>
    <ul class="arrow-list">
      <li>Genetische Überempfindlichkeit auf weibliche Hormone</li>
      <li>Medikamente</li>
      <li>Anabolika/ Steroide</li>
      <li>Ungünstige Fettverteilung</li>
    </ul>
    <p>Oftmals reicht die Absaugung des überschüssigen Gewebes. Selbst vergrößerte Brustwarzen können sich dadurch zurückbilden, sonst hilft eine Hautstraffung.</p>
  </div>

  <div class="panel">
    <h2 class="section-title"><span>Straffungen</span></h2>
    <h3 class="sub-title">Bauchdeckenstraffung</h3>
    <p>Nach Gewichtsverlust oder Schwangerschaft kann es zu einem Überschuss an Haut und Gewebe im Bauchbereich kommen. Hier kann eine Bauchdeckenstraffung Abhilfe schaffen. Oftmals ist auch eine Rektusdiastase mitbehandelbar. Die Narben liegen gut versteckt im Bereich der Unterwäsche.</p>
    <h3 class="sub-title" style="margin-top:18px">Oberarmstraffung</h3>
    <p>Die Haut an den Oberarmen ist sehr dünn und verliert im Laufe des Lebens an Elastizität. Oftmals ist die operative Hautstraffung die sinnvollste Therapie. Die Narben werden so gelegt, dass sie kaum sichtbar sind.</p>
    <h3 class="sub-title" style="margin-top:18px">Oberschenkelstraffung</h3>
    <p>Auch die Haut an den inneren Oberschenkeln ist dünn. Je nach Befund kommen drei Straffungsmethoden zum Einsatz. Die Narben liegen in der Leiste oder an der Innenseite.</p>
    <div class="brand inside-brand">Lumenhaut</div>
  </div>
</section>

</body>
</html>
```